Pelican Shoals Postcard Design

I am a real estate agent
I am marketing a gulf access waterfront community is southwest florida. I would like to do Just Listed and Just Sold post cards

So this will be two different post cards

In addition to the pictures I have uploaded mock ups of an idea of what I would like for the front and the back

I would like this done glossy on both sides

```html
<!DOCTYPE html>
<html lang="en">
<head>
<meta charset="UTF-8">
<title>Pelican Shoals Just Listed Postcard – Back</title>
<link rel="stylesheet" href="https://fonts.googleapis.com/css2?family=Quicksand:wght@500;600&family=PT+Sans+Narrow:wght@700&display=swap">
<style>
  :root {
    --page-bg: #ffffff;
    --sky-top: #e2f3fb;
    --sky-mid: #dcecf3;
    --haze: #cfdde0;
    --land: #c4d0cc;
    --land-deep: #b6c3c2;
    --tab-border: #ffffff;
    --tab-top: #262061;
    --tab-bottom: #1a76bd;
    --tab-text: #ffffff;
    --body-text: #3b3b3d;
    --rule: #3b3b3d;
    --stamp-line: #8c8f92;
  }
  * { margin: 0; padding: 0; box-sizing: border-box; }
  html, body {
    width: 1200px;
    height: 1000px;
    overflow: hidden;
    background: var(--page-bg);
  }
  .postcard {
    position: absolute;
    left: 67px;
    top: 33px;
    width: 1086px;
    height: 842px;
    overflow: hidden;
  }
  .aerial-backdrop {
    position: absolute;
    inset: 0;
    background: linear-gradient(180deg,
      var(--sky-top) 0%,
      var(--sky-mid) 30%,
      var(--haze) 44%,
      var(--land) 62%,
      var(--land-deep) 100%);
  }
  .agent-tab {
    position: absolute;
    left: 45px;
    top: -12px;
    width: 440px;
    height: 251px;
    background: var(--tab-border);
    border-radius: 0 0 26px 26px;
    padding: 0 7px 7px;
    box-shadow: 0 2px 6px rgba(0,0,0,0.15);
  }
  .agent-tab-inner {
    width: 100%;
    height: 100%;
    border-radius: 0 0 20px 20px;
    background: linear-gradient(180deg, var(--tab-top) 0%, var(--tab-bottom) 100%);
    color: var(--tab-text);
    font-family: "Quicksand", sans-serif;
    text-align: center;
    padding-top: 53px;
  }
  .agent-name {
    font-size: 40px;
    font-weight: 600;
    letter-spacing: 0.5px;
    line-height: 42px;
  }
  .agent-brokerage {
    font-size: 26px;
    font-weight: 600;
    line-height: 34px;
    letter-spacing: 0.3px;
  }
  .agent-address {
    font-size: 28px;
    font-weight: 500;
    line-height: 37px;
    margin-top: 12px;
  }
  .stamp-box {
    position: absolute;
    left: 819px;
    top: 31px;
    width: 238px;
    height: 238px;
    border: 1.5px solid var(--stamp-line);
  }
  .listing-message {
    position: absolute;
    left: 58px;
    top: 336px;
    font-family: "PT Sans Narrow", sans-serif;
    font-weight: 700;
    color: var(--body-text);
  }
  .fill-line {
    display: inline-block;
    border-bottom: 2px solid var(--rule);
    vertical-align: baseline;
  }
  .address-line { width: 451px; height: 2px; border-bottom: 2px solid var(--rule); }
  .announce {
    font-size: 22px;
    margin-top: 22px;
    line-height: 30px;
  }
  .price-row {
    font-size: 22px;
    margin-top: 40px;
    line-height: 30px;
  }
  .price-row .price-blank { width: 170px; margin: 0 12px 0 4px; height: 20px; }
  .price-row .date-blank { width: 170px; margin-left: 20px; height: 20px; }
  .invite {
    font-size: 22px;
    line-height: 35px;
    margin-top: 40px;
  }
  .contact {
    margin-top: 26px;
    font-size: 34px;
    line-height: 42px;
  }
</style>
</head>
<body>
  <section class="postcard">
    <div class="aerial-backdrop" role="img" aria-label="Faded aerial photograph of the Pelican Shoals waterfront canals and streets under a pale sky"></div>

    <header class="agent-tab">
      <div class="agent-tab-inner">
        <div class="agent-name">MAREN ELLIS</div>
        <div class="agent-brokerage">HARBOR TIDE REALTY</div>
        <div class="agent-address">PO Box 418<br>Palm Inlet, FL 33900</div>
      </div>
    </header>

    <div class="stamp-box" aria-label="Stamp area"></div>

    <div class="listing-message">
      <div class="address-line"></div>
      <p class="announce">on your block of Pelican Shoals has just LISTED</p>
      <p class="price-row">at $ <span class="fill-line price-blank"></span> on <span class="fill-line date-blank"></span></p>
      <p class="invite">Please contact me if you are interested in<br>buying or selling property in the area.</p>
      <p class="contact">941.555.0142<br>marenellis@tidemail.com</p>
    </div>
  </section>
</body>
</html>
```